Business Card Project

We are a small consulting firm. You can experiment with any design.
Must have:
1) Company name - OLUNDEX International
2) Company slogan - simple solutions for complex problems
3) Name/Title/Phone/Email/WWW/ - use anything you like as an example.

Industry/Entity Type

Business

```html
<!DOCTYPE html>
<html lang="en">
<head>
<meta charset="utf-8">
<title>OLUNDEX International – Business Card</title>
<link rel="stylesheet" href="https://fonts.googleapis.com/css2?family=Questrial&display=swap">
<style>
  :root {
    --page-bg: #c8cfd6;
    --card-white: #ffffff;
    --band-dark: #3b3b3b;
    --brand-grey: #4a4a4a;
    --accent-blue: #2b8fda;
    --text-light: #e6e6e6;
    --text-muted: #b9b9b9;
  }
  * { margin: 0; padding: 0; box-sizing: border-box; }
  html, body {
    width: 1200px;
    height: 848px;
    overflow: hidden;
    background: var(--page-bg);
    font-family: "Questrial", Arial, sans-serif;
  }
  .card {
    position: absolute;
    left: 110px;
    top: 144px;
    width: 980px;
    height: 560px;
    background: var(--card-white);
    box-shadow: 0 6px 18px rgba(0, 0, 0, 0.18);
    overflow: hidden;
  }
  .brand {
    position: absolute;
    left: 56px;
    top: 60px;
    display: flex;
    align-items: center;
    gap: 38px;
  }
  .brand-dot {
    width: 128px;
    height: 128px;
    border-radius: 50%;
    background: var(--accent-blue);
    flex: none;
  }
  .brand-name {
    color: var(--brand-grey);
    font-weight: 400;
    line-height: 1;
  }
  .brand-name .word-main {
    display: block;
    font-size: 100px;
    letter-spacing: 2px;
  }
  .brand-name .word-sub {
    display: block;
    margin-top: 6px;
    font-size: 30px;
    letter-spacing: 14px;
  }
  .details-band {
    position: absolute;
    left: 0;
    right: 0;
    top: 262px;
    bottom: 0;
    background: var(--band-dark);
  }
  .person {
    position: absolute;
    left: 52px;
    top: 42px;
    display: flex;
    align-items: baseline;
    gap: 14px;
  }
  .person-name {
    color: var(--accent-blue);
    font-size: 38px;
    letter-spacing: 0.5px;
  }
  .person-title {
    color: var(--text-light);
    font-size: 30px;
    padding-left: 8px;
    border-left: 2px solid var(--accent-blue);
    line-height: 1;
  }
  .slogan {
    position: absolute;
    left: 52px;
    top: 104px;
    color: var(--text-muted);
    font-size: 21px;
    letter-spacing: 1px;
  }
  .contacts {
    position: absolute;
    left: 52px;
    top: 164px;
    list-style: none;
    font-size: 25px;
    line-height: 38px;
  }
  .contacts li { display: flex; }
  .contact-key {
    width: 46px;
    color: var(--accent-blue);
  }
  .contact-value { color: var(--text-light); }
</style>
</head>
<body>
  <article class="card">
    <header class="brand">
      <div class="brand-dot"></div>
      <h1 class="brand-name">
        <span class="word-main">OLUNDEX</span>
        <span class="word-sub">INTERNATIONAL</span>
      </h1>
    </header>
    <section class="details-band">
      <div class="person">
        <span class="person-name">DANIEL BROOKS</span>
        <span class="person-title">Manager</span>
      </div>
      <p class="slogan">simple solutions for complex problems</p>
      <ul class="contacts">
        <li><span class="contact-key">T</span><span class="contact-value">:0198765432</span></li>
        <li><span class="contact-key">E</span><span class="contact-value">:OLUNDEXinternational@mailbox.com</span></li>
        <li><span class="contact-key">W</span><span class="contact-value">:www.OLUNDEXinternational.com</span></li>
      </ul>
    </section>
  </article>
</body>
</html>
```